brisknest

i want to ues this logo and the same colors used on the business card

cleaning & service

Industry/Entity Type

Business

Contact Information for Business Card

Font styles to use
Serif
Sans Serif
Decorative
Script

Colors
add136
0692cd
000000
5c5c5c
fbfbfb

Requirements
Must have
• cleaning things

```html
<!DOCTYPE html>
<html lang="en">
<head>
<meta charset="utf-8">
<title>Brisknest Business Card</title>
<link rel="stylesheet" href="https://fonts.googleapis.com/css2?family=Open+Sans:wght@400;600;700&display=swap">
<style>
  :root {
    --brand-green: #add136;
    --brand-blue: #0692cd;
    --ink: #000000;
    --ink-soft: #5c5c5c;
    --paper: #fbfbfb;
    --stage: #e9eaec;
    --card-shadow: rgba(0, 0, 0, 0.12);
  }
  * { box-sizing: border-box; margin: 0; padding: 0; }
  html, body {
    width: 1200px;
    height: 900px;
    overflow: hidden;
    background: var(--stage);
    font-family: "Open Sans", Arial, sans-serif;
  }
  .stage {
    position: relative;
    width: 1200px;
    height: 900px;
  }
  .card {
    position: absolute;
    width: 500px;
    height: 286px;
    background: var(--paper);
    box-shadow: 0 10px 28px var(--card-shadow);
  }
  .card--info { left: 70px; top: 307px; }
  .card--brand { left: 630px; top: 307px; }

  .person {
    position: absolute;
    left: 34px;
    top: 30px;
  }
  .person__name {
    color: var(--brand-blue);
    font-weight: 600;
    font-size: 15px;
    letter-spacing: 0.4px;
    text-transform: uppercase;
    line-height: 1.2;
  }
  .person__role {
    color: var(--ink);
    font-size: 11.5px;
    line-height: 1.3;
  }
  .contact {
    position: absolute;
    left: 34px;
    top: 112px;
    list-style: none;
  }
  .contact__item {
    display: flex;
    align-items: center;
    gap: 7px;
    color: var(--ink-soft);
    font-size: 12px;
    line-height: 18px;
  }
  .contact__icon {
    width: 11px;
    height: 11px;
    fill: var(--brand-blue);
    flex: none;
  }

  .brand-mark {
    position: absolute;
    display: flex;
    align-items: center;
    gap: 10px;
  }
  .brand-mark__motif {
    flex: none;
    width: 40px;
    height: 40px;
    border-radius: 6px;
    background: linear-gradient(135deg, var(--brand-green) 0%, var(--brand-green) 45%, var(--brand-blue) 100%);
  }
  .brand-mark__name {
    color: var(--brand-blue);
    font-weight: 700;
    letter-spacing: 0.2px;
    white-space: nowrap;
  }
  .card--info .brand-mark { right: 34px; bottom: 44px; }
  .card--info .brand-mark__name { font-size: 22px; }
  .card--brand .brand-mark {
    left: 50%;
    top: 50%;
    transform: translate(-50%, -50%);
    gap: 12px;
  }
  .card--brand .brand-mark__motif { width: 54px; height: 54px; }
  .card--brand .brand-mark__name { font-size: 30px; }
</style>
</head>
<body>
<main class="stage">
  <section class="card card--info" aria-label="Business card, contact side">
    <div class="person">
      <p class="person__name">Marcus Hale</p>
      <p class="person__role">Managing Director</p>
    </div>
    <ul class="contact">
      <li class="contact__item">
        <svg class="contact__icon" viewBox="0 0 24 24" aria-hidden="true"><path d="M6.6 10.8a15.1 15.1 0 0 0 6.6 6.6l2.2-2.2c.3-.3.7-.4 1-.2 1.1.4 2.3.6 3.6.6.6 0 1 .4 1 1V20c0 .6-.4 1-1 1A17 17 0 0 1 3 4c0-.6.4-1 1-1h3.5c.6 0 1 .4 1 1 0 1.3.2 2.5.6 3.6.1.3 0 .7-.2 1z"/></svg>
        <span>(044)555018273</span>
      </li>
      <li class="contact__item">
        <svg class="contact__icon" viewBox="0 0 24 24" aria-hidden="true"><path d="M2 5h20v14H2z M4 7v.5l8 5 8-5V7z" fill-rule="evenodd"/></svg>
        <span>hello@brisknest.com</span>
      </li>
    </ul>
    <div class="brand-mark">
      <span class="brand-mark__motif" role="img" aria-label="Cleaning motif: green broom and blue sparkles"></span>
      <span class="brand-mark__name">brisknest</span>
    </div>
  </section>

  <section class="card card--brand" aria-label="Business card, brand side">
    <div class="brand-mark">
      <span class="brand-mark__motif" role="img" aria-label="Cleaning motif: green broom and blue sparkles"></span>
      <span class="brand-mark__name">brisknest</span>
    </div>
  </section>
</main>
</body>
</html>
```